Lark Vale Perks Needs a Website Design

We need a website design for a new service we are starting. Users enter a coupon in a redemption page and either create an account or sign in. they can then use the credits they accumulate from the coupons to purchase items listed on the site.

we need a design for the following:
-the coupon redemption page (with a choice to either sign in or create an account)
-a product listing page (with search filters and a search bar. the search bar can be displayed in the header of the site)
-a product detail page, showing the product's title, image, credit redemption value, brand and any category associated with the item
-a my account page, with:
*a list of the pluses (coupons/credit added to account) and the minuses (orders placed/credits subtracted from account) to show a detailed description of their history on the site)
*an area for users to edit their name, phone number, address etc
*an area for users to add / edit their casino membership number and casino
*an area for users to add a coupon to their account
-a cart / checkout process:
*cart displaying items and their total
*entering / selecting an address from their account
*review order details page where they can submit their order (and warning the user that doing so will subtract the required credits from their account)

remember that no ecommerce or money is used on the site.. users are spending their credits and checkout their cart with the credits they accumulated, so the items each have a credit redemption value and the checkout process is shown in credits.

we are not very particular with any design preference, other than we'd like it to be predominately white.

If designing the site with css please make sure to use bootstrap in your designs. thanks!

Target Market(s)

adults 45-65

Industry/Entity Type

Casino

Coding

Coded - Design and coding required

Number of Pages Required

5+ page

Font styles to use
Sans Serif

Requirements
Must have
• css must use with bootstrap
Nice to have
• simplified, easy interface. we are targeting an older crowd and dont want to confuse them
Should not have
• the site shouldnt have any dollar values. all product prices, checkout totals and user accrual's (in the my account page) should be in credits

```html
<!DOCTYPE html>
<html lang="en">
<head>
<meta charset="utf-8">
<title>Lark Vale Perks</title>
<link rel="stylesheet" href="https://fonts.googleapis.com/css2?family=Open+Sans:wght@400;600;700;800&display=swap">
<style>
:root{
  --blue:#0b6bc2;
  --blue-dark:#08569c;
  --red:#d32f2b;
  --ink:#2e2e2e;
  --muted:#8a8a8a;
  --line:#e2e2e2;
  --soft:#f3f3f3;
  --panel:#fafafa;
  --white:#ffffff;
  --dark-bar:#3a3a3a;
}
*{box-sizing:border-box;margin:0;padding:0}
html,body{width:706px;height:1200px;overflow:hidden;background:var(--white)}
body{font-family:"Open Sans",Arial,sans-serif;color:var(--ink);font-size:6px;position:relative}
.abs{position:absolute}

/* header */
.site-header{left:0;top:0;width:706px;height:52px}
.brand{left:36px;top:15px;font-weight:600;font-size:15px;color:var(--ink);letter-spacing:.2px}
.search{left:370px;top:16px;display:flex;align-items:center;gap:3px}
.search-field{width:190px;height:13px;border:1px solid var(--line);font-size:5px;color:var(--muted);padding:3px 4px}
.search-btn{width:13px;height:13px;background:var(--blue)}
.sign-in{height:13px;padding:0 7px;border:1px solid var(--blue);color:var(--blue);font-size:5px;font-weight:700;line-height:11px;margin-left:3px}

.main-nav{left:36px;top:55px;width:634px;height:18px;background:var(--soft);display:flex;border-bottom:2px solid var(--blue)}
.main-nav span{flex:1;text-align:center;font-size:5px;font-weight:600;color:#666;line-height:18px}
.main-nav .active{background:var(--blue);color:var(--white)}

/* sidebar */
.side-box{left:36px;width:84px;border:1px solid var(--line);background:var(--white)}
.side-head{background:var(--red);color:var(--white);font-weight:700;font-size:5.5px;padding:5px 6px}
.side-list{list-style:none;padding:4px 6px}
.side-list li{font-size:4.6px;color:#666;padding:4.5px 0 4.5px 7px;border-bottom:1px solid #efefef;position:relative}
.side-list li::before{content:"";position:absolute;left:0;top:7px;width:3px;height:3px;background:#bbb}
.side-list li.sub{padding-left:14px;color:#999}
.side-list li.sub::before{left:8px;background:#ddd}
.side-filter .side-list li{padding:5.5px 0 5.5px 7px}
.side-filter .side-list li.sub{padding-left:14px}
.side-filter .side-list li::before{top:8px}
.side-promo{left:36px;top:598px;width:84px}
.side-photo{width:84px;height:50px;background:linear-gradient(135deg,#c7dbe6,#e6d3c2)}
.side-caption{text-align:center;font-size:4.6px;color:#666;margin-top:4px}
.side-caption b{display:block;color:var(--red);margin-top:1px;font-weight:600}

/* hero */
.hero{left:128px;top:90px;width:542px;height:230px;background:linear-gradient(100deg,#5f6f7c 0%,#a9b7bf 45%,#e6ddd0 100%)}
.hero-copy{left:16px;top:92px;color:var(--white)}
.hero-title{font-size:16px;font-weight:800;letter-spacing:.5px}
.hero-sub{font-size:5.5px;margin-top:3px;font-weight:600}
.hero-text{font-size:4.5px;margin-top:4px;width:140px;line-height:1.5;opacity:.9}
.btn-red{display:inline-block;background:var(--red);color:var(--white);font-weight:700;font-size:4.6px;padding:4px 8px}
.hero .btn-red{margin-top:8px}

/* features */
.features{left:128px;top:335px;width:542px;height:52px;display:flex;gap:8px}
.feature{flex:1;border:1px solid var(--line);display:flex;gap:7px;padding:9px}
.feature-icon{width:16px;height:16px;border-radius:50%;background:var(--blue);flex:none;display:flex;align-items:center;justify-content:center}
.feature h4{font-size:5px;color:var(--blue);font-weight:700}
.feature p{font-size:4.3px;color:var(--muted);line-height:1.5;margin-top:2px}

/* our products */
.products{left:128px;top:400px;width:542px;height:222px;border:1px solid var(--line)}
.bar-head{background:var(--dark-bar);color:var(--white);font-weight:700;font-size:5px;padding:5px 8px}
.product-row{display:flex;gap:12px;padding:12px 12px}
.product-card{flex:1;border:1px solid var(--line);height:180px;text-align:center;padding-top:14px}
.product-card h5{font-size:5px;color:var(--blue);font-weight:600}
.product-img{width:50px;height:64px;margin:18px auto 20px;border-radius:3px}
.img-phone{background:linear-gradient(#444,#1d1d1d)}
.img-watch{width:60px;height:60px;background:linear-gradient(#9aa3ab,#4d555c);border-radius:50%}
.img-bag{width:56px;background:linear-gradient(#9fd5ea,#5fb2d3)}
.credits{font-size:4.3px;color:#666;font-weight:600}
.product-card .btn-red{margin-top:8px;font-size:4.2px;padding:3px 7px}

/* promo strip */
.promo{left:128px;top:632px;width:542px;height:74px;background:var(--panel);border:1px solid var(--line);display:flex;align-items:center;gap:12px;padding:0 10px}
.promo-img{width:64px;height:54px;background:linear-gradient(135deg,#d7b48d,#a98055);flex:none}
.promo-copy h3{font-size:7px;font-weight:800;color:#444}
.promo-copy .earn{font-size:5.5px;color:#555;margin-top:2px}
.promo-copy .earn b{color:var(--red)}
.promo-copy p{font-size:4.3px;color:var(--muted);margin-top:3px;width:300px;line-height:1.5}
.promo .btn-red{margin-left:auto}

/* product list band */
.band{left:0;top:730px;width:706px;height:188px;background:var(--blue)}
.band h2{position:absolute;top:22px;width:100%;text-align:center;color:var(--white);font-size:9px;font-weight:700;letter-spacing:.5px}
.band-row{position:absolute;left:36px;top:58px;width:634px;display:flex;gap:16px}
.band-card{flex:1;height:106px;background:var(--white);padding:10px;text-align:center}
.band-img{height:70px;margin-bottom:8px}
.img-handbag{background:linear-gradient(#e2684a,#b63d25);border-radius:6px}
.img-monitor{background:linear-gradient(#6fb4d9,#2e6f9c)}
.img-clock{background:radial-gradient(circle,#555 40%,#fff 42%)}
.img-tablet{background:linear-gradient(#3a3a3a,#111);border-radius:4px}
.band-card span{font-size:4.6px;color:var(--blue);font-weight:700}

/* partners */
.partners{left:36px;top:944px;width:634px;height:46px;display:flex;justify-content:space-between;align-items:center;padding:0 14px}
.partner-badge{width:76px;height:18px;background:#d9d9d9;border-radius:3px}

/* footer */
.site-footer{left:0;top:1005px;width:706px;height:150px;background:var(--white);border-top:1px solid var(--line)}
.footer-cols{position:absolute;left:36px;top:22px;width:634px;display:flex;gap:20px}
.footer-col{flex:1}
.footer-col.wide{flex:1.5}
.footer-col h6{font-size:5.5px;font-weight:700;color:#444;margin-bottom:6px}
.footer-col li{list-style:none;font-size:4.6px;color:var(--muted);padding:2.5px 0}
.footer-col p{font-size:4.6px;color:var(--muted);line-height:1.6}
.pay-row{display:flex;gap:4px;margin-top:8px}
.pay-row i{width:18px;height:11px;background:#c8c8c8;border-radius:2px}
.contact-line{display:flex;align-items:center;gap:4px;font-size:4.6px;color:var(--muted);padding:3px 0}
.contact-line svg{flex:none}
.bottom-bar{left:36px;top:1160px;width:634px;height:30px;display:flex;align-items:center;justify-content:space-between;border-top:1px solid var(--line)}
.bottom-bar p{font-size:4.6px;color:var(--muted)}
.social{display:flex;gap:4px;align-items:center;font-size:4.6px;color:var(--muted)}
.social i{width:9px;height:9px;background:var(--blue);border-radius:1px}
</style>
</head>
<body>

<header class="site-header abs">
  <div class="brand abs">Lark Vale Perks</div>
  <div class="search abs">
    <div class="search-field">Search products…</div>
    <div class="search-btn"></div>
    <div class="sign-in">SIGN IN</div>
  </div>
</header>

<nav class="main-nav abs">
  <span class="active">HOME</span><span>ABOUT US</span><span>WEBSITE</span><span>PRODUCTS</span><span>REWARDS</span><span>SERVICES</span><span>BLOG</span><span>CONTACT US</span>
</nav>

<aside class="side-box abs" style="top:90px;height:230px">
  <div class="side-head">CATEGORY</div>
  <ul class="side-list">
    <li>Gift Cards</li><li>Home Goods</li><li>Kitchen Ware</li><li>Electronics</li><li>Watches</li><li>Travel Bags</li><li>Jewelry Items</li><li>Golf Gear</li><li>Dining Offers</li><li>Spa Packages</li><li>Outdoor Living</li>
  </ul>
</aside>

<aside class="side-box side-filter abs" style="top:335px;height:250px">
  <div class="side-head">FILTER</div>
  <ul class="side-list">
    <li>Credit Range</li><li class="sub">Under 1000</li><li class="sub">1000 to 2500</li><li class="sub">2500 to 5000</li><li class="sub">Over 5000</li>
    <li>Brand</li><li class="sub">Brand One</li><li class="sub">Brand Two</li><li class="sub">Brand Three</li>
    <li>Newest Items</li><li>Most Popular</li>
  </ul>
</aside>

<div class="side-promo abs">
  <div class="side-photo" role="img" aria-label="Photo of a member enjoying a reward"></div>
  <div class="side-caption">Tempor cum laude rewards<b>Learn More</b></div>
</div>

<section class="hero abs" role="img" aria-label="Photo of a smiling member at a laptop in a bright room">
  <div class="hero-copy abs">
    <div class="hero-title">LARK VALE PERKS</div>
    <div class="hero-sub">EXPLORE BY THE TRUTH, THE MASTER</div>
    <div class="hero-text">Redeem your coupons and spend your credits on rewards you love.</div>
    <span class="btn-red">VIEW PRODUCTS</span>
  </div>
</section>

<section class="features abs">
  <div class="feature">
    <div class="feature-icon"><svg width="8" height="8" viewBox="0 0 8 8"><rect x="1" y="2" width="6" height="4" fill="#fff"/></svg></div>
    <div><h4>LOGIN</h4><p>Sign in to see your credit balance and history.</p></div>
  </div>
  <div class="feature">
    <div class="feature-icon"><svg width="8" height="8" viewBox="0 0 8 8"><path d="M2 1l4 3-4 3z" fill="#fff"/></svg></div>
    <div><h4>SELECT</h4><p>Browse items and add them to your cart.</p></div>
  </div>
  <div class="feature">
    <div class="feature-icon"><svg width="8" height="8" viewBox="0 0 8 8"><path d="M1 4l2 2 4-4" stroke="#fff" stroke-width="1.4" fill="none"/></svg></div>
    <div><h4>SHIP</h4><p>Confirm your order and we deliver it home.</p></div>
  </div>
</section>

<section class="products abs">
  <div class="bar-head">OUR PRODUCTS</div>
  <div class="product-row">
    <div class="product-card"><h5>Culpa Officia Deserunt</h5><div class="product-img img-phone" role="img" aria-label="Smartphone product photo"></div><div class="credits">2500 CREDITS</div><span class="btn-red">REDEEM NOW</span></div>
    <div class="product-card"><h5>Culpa Officia Deserunt</h5><div class="product-img img-watch" role="img" aria-label="Wristwatch product photo"></div><div class="credits">3200 CREDITS</div><span class="btn-red">REDEEM NOW</span></div>
    <div class="product-card"><h5>Culpa Officia Deserunt</h5><div class="product-img img-bag" role="img" aria-label="Handbag product photo"></div><div class="credits">1800 CREDITS</div><span class="btn-red">REDEEM NOW</span></div>
  </div>
</section>

<section class="promo abs">
  <div class="promo-img" role="img" aria-label="Photo of gift boxes"></div>
  <div class="promo-copy">
    <h3>EXCEPTEUR EST OMNIS DOLOR REPELLENDUS.</h3>
    <div class="earn">Earn upto <b>10 Points</b> per 100 credits</div>
    <p>Quis autem vel eum iure reprehenderit qui in ea voluptate velit esse quam nihil molestiae consequatur.</p>
  </div>
  <span class="btn-red">REDEEM NOW</span>
</section>

<section class="band abs">
  <h2>PRODUCT LIST</h2>
  <div class="band-row">
    <div class="band-card"><div class="band-img img-handbag" role="img" aria-label="Leather handbag product photo"></div><span>CUM DOLORE DEMO</span></div>
    <div class="band-card"><div class="band-img img-monitor" role="img" aria-label="Desktop computer product photo"></div><span>CUM DOLORE DEMO</span></div>
    <div class="band-card"><div class="band-img img-clock" role="img" aria-label="Wristwatch product photo"></div><span>CUM DOLORE DEMO</span></div>
    <div class="band-card"><div class="band-img img-tablet" role="img" aria-label="Tablet product photo"></div><span>CUM DOLORE DEMO</span></div>
  </div>
</section>

<section class="partners abs">
  <i class="partner-badge"></i><i class="partner-badge"></i><i class="partner-badge"></i><i class="partner-badge"></i><i class="partner-badge"></i>
</section>

<footer class="site-footer abs">
  <div class="footer-cols">
    <div class="footer-col wide">
      <h6>LARK VALE PERKS</h6>
      <p>Spend the credits you earn on rewards for home, travel and leisure. No money needed, only credits.</p>
      <div class="pay-row"><i></i><i></i><i></i><i></i></div>
    </div>
    <div class="footer-col"><h6>QUICK LINKS</h6><ul><li>Home</li><li>About Us</li><li>Products</li><li>Rewards</li><li>Contact</li></ul></div>
    <div class="footer-col"><h6>EXTRAS</h6><ul><li>Brands</li><li>Gift Cards</li><li>Specials</li><li>Site Map</li><li>Help Desk</li></ul></div>
    <div class="footer-col"><h6>MY ACCOUNT</h6><ul><li>My Account</li><li>Order History</li><li>Add Coupon</li><li>My Cart</li><li>Sign Out</li></ul></div>
    <div class="footer-col wide"><h6>CONTACT US</h6>
      <div class="contact-line"><svg width="6" height="6" viewBox="0 0 6 6"><path d="M3 0a2 2 0 0 1 2 2c0 1.5-2 4-2 4S1 3.5 1 2a2 2 0 0 1 2-2z" fill="#999"/></svg>12 Harbor Lane, Lark Vale</div>
      <div class="contact-line"><svg width="6" height="6" viewBox="0 0 6 6"><path d="M1 0h1.5l.5 1.5-1 .7a4 4 0 0 0 1.8 1.8l.7-1L6 3.5V5a1 1 0 0 1-1 1A5 5 0 0 1 0 1a1 1 0 0 1 1-1z" fill="#999"/></svg>(555) 014-2280</div>
      <div class="contact-line"><svg width="6" height="6" viewBox="0 0 6 6"><rect x=".5" y="1" width="5" height="4" fill="none" stroke="#999" stroke-width=".8"/><path d="M.5 1L3 3l2.5-2" fill="none" stroke="#999" stroke-width=".8"/></svg>help@larkvaleperks.example</div>
    </div>
  </div>
</footer>

<div class="bottom-bar abs">
  <p>Copyright © 2015 Lark Vale Perks. All Rights Reserved.</p>
  <div class="social">Follow us <i></i><i></i><i></i><i></i></div>
</div>

</body>
</html>
```